Ledgers On Track Business Card Design

We are a bookkeeping and accounting practice and are particularly passionate about Tallivo as 'state of the art' accounting software. We offer a number of services which are listed on the back of the card. The logos for LOT have already been developed. There are also other logos of organisations we are involved with - Tallivo (both certified advisor and silver partner), FKR, and dutyfile near. Regarding colours, we would like to use the colours similar to our website, www.ledgersontrack.com, and these connect with the www.tallivo.com.au website. The proposed layout as it is just does not look too great - it looks like an amateur has done it - which is true!

Industry/Entity Type

Accounting

Contact Information for Business Card

The details to appear on the card are found on the files uploaded. I have front and back rough layouts.

```html
<!DOCTYPE html>
<html lang="en">
<head>
<meta charset="utf-8">
<title>Ledgers On Track – Business Card</title>
<link href="https://fonts.googleapis.com/css2?family=Bitter:wght@700&family=Crimson+Text:wght@400;600&display=swap" rel="stylesheet">
<style>
  :root {
    --page-bg: #ecebe7;
    --card-white: #ffffff;
    --brand-blue: #3f5497;
    --panel-blue: #3b4f8e;
    --brand-green: #5aaa3c;
    --tick-green: #6cc04a;
    --text-grey: #6a6a6a;
    --text-dark: #3c3c3c;
    --badge-cyan: #1bb4d8;
    --badge-teal: #1593ad;
    --badge-grey: #a9a9a9;
  }
  * { box-sizing: border-box; margin: 0; padding: 0; }
  html, body { width: 1200px; height: 1023px; overflow: hidden; background: var(--page-bg); }
  body { font-family: "Crimson Text", Georgia, serif; color: var(--text-dark); position: relative; }

  .card {
    position: absolute; left: 170px; width: 860px; height: 470px;
    background: var(--card-white); overflow: hidden;
    box-shadow: 0 6px 18px rgba(0,0,0,0.18);
  }
  .card--back { top: 28px; display: flex; }
  .card--front { top: 525px; }

  /* ---------- Brand wordmark ---------- */
  .wordmark {
    font-family: "Bitter", Georgia, serif; font-weight: 700; color: var(--brand-blue);
    display: flex; align-items: center; gap: 14px; line-height: 1.02;
  }
  .wordmark__dot { width: 22px; height: 22px; border-radius: 50%; background: var(--brand-green); flex: none; }

  /* ---------- Partner names and plain badges ---------- */
  .org-name {
    font-family: "Crimson Text", Georgia, serif; font-weight: 600; color: var(--text-dark);
    display: flex; align-items: center; gap: 10px; line-height: 1;
  }
  .org-name__square { width: 18px; height: 18px; background: var(--badge-grey); flex: none; }
  .badge { border-radius: 50%; flex: none; }
  .badge--partner { background: var(--badge-grey); }
  .badge--advisor { background: var(--badge-teal); }
  .badge--listing { background: var(--badge-cyan); }

  /* ---------- Back ---------- */
  .back-brand {
    width: 340px; padding: 60px 0 0 52px; display: flex; flex-direction: column; gap: 26px;
  }
  .back-brand .wordmark { font-size: 40px; }
  .back-partners { display: flex; align-items: center; gap: 18px; }
  .back-partners .org-name { font-size: 32px; }
  .back-partners .badge { width: 96px; height: 96px; }
  .back-brand .org-name--fkr { font-size: 30px; }
  .back-brand .org-name--dutyfile { font-size: 32px; }

  .services {
    flex: 1; background: var(--panel-blue); list-style: none;
    clip-path: polygon(14% 0, 100% 0, 100% 100%, 22% 100%);
    padding: 46px 16px 0 86px; display: flex; flex-direction: column; gap: 9px;
  }
  .service { display: flex; gap: 9px; color: #fff; font-size: 20px; line-height: 1.15; white-space: nowrap; }
  .service svg { flex: none; width: 20px; height: 20px; margin-top: 3px; }
  .service__name { color: var(--tick-green); font-weight: 600; font-size: 22px; }
  .service:nth-child(2) { margin-left: 14px; }
  .service:nth-child(3) { margin-left: 26px; }
  .service:nth-child(4) { margin-left: 38px; }
  .service:nth-child(5) { margin-left: 50px; }
  .service:nth-child(6) { margin-left: 62px; }
  .service:nth-child(7) { margin-left: 74px; }

  /* ---------- Front ---------- */
  .front-title { position: absolute; left: 46px; top: 52px; font-size: 64px; }
  .front-title .wordmark__dot { width: 40px; height: 40px; }
  .abn { position: absolute; left: 72px; top: 146px; font-size: 20px; color: var(--text-grey); letter-spacing: 0.5px; }

  .person { position: absolute; left: 64px; top: 200px; width: 290px; text-align: center; }
  .person__name { font-weight: 600; font-size: 38px; color: var(--brand-green); line-height: 1.1; }
  .person__credentials { font-size: 23px; color: var(--text-grey); line-height: 1.15; margin-top: 4px; }

  .front-partners { position: absolute; left: 62px; top: 345px; display: flex; align-items: center; gap: 22px; }
  .front-partners .org-name { font-size: 36px; }
  .front-partners .badge { width: 104px; height: 104px; }

  .contact { position: absolute; left: 470px; top: 210px; list-style: none; font-size: 21px; line-height: 1.1; color: var(--text-dark); }
  .contact li { display: flex; align-items: flex-start; gap: 9px; margin-bottom: 3px; }
  .contact__icon {
    width: 17px; height: 17px; border-radius: 3px; background: var(--brand-green);
    flex: none; margin-top: 4px; display: flex; align-items: center; justify-content: center;
  }
  .contact__icon svg { width: 12px; height: 12px; }
  .contact__phones { display: flex; gap: 10px; }
  .contact__phones span { display: flex; gap: 9px; }

  .front-fkr { position: absolute; left: 470px; top: 378px; font-size: 30px; }
  .front-stripe { position: absolute; left: 0; right: 0; bottom: 0; height: 12px; background: var(--brand-blue); }
</style>
</head>
<body>

<section class="card card--back" aria-label="Card back">
  <div class="back-brand">
    <div class="wordmark"><span class="wordmark__dot"></span><span>Ledgers<br>On Track</span></div>
    <div class="back-partners">
      <div class="org-name">Tallivo</div>
      <div class="badge badge--partner" role="img" aria-label="Silver partner badge"></div>
    </div>
    <div class="org-name org-name--fkr"><span class="org-name__square"></span>FKR</div>
    <div class="org-name org-name--dutyfile">dutyfile near</div>
  </div>
  <ul class="services">
    <li class="service"><svg viewBox="0 0 24 24"><path d="M3 13l6 6L22 4" fill="none" stroke="#6cc04a" stroke-width="4"/></svg><span><span class="service__name">Bookkeeping</span> - data entry,<br>bank reconciliation and review</span></li>
    <li class="service"><svg viewBox="0 0 24 24"><path d="M3 13l6 6L22 4" fill="none" stroke="#6cc04a" stroke-width="4"/></svg><span><span class="service__name">Payroll</span> - Tallivo Payroll Specialist</span></li>
    <li class="service"><svg viewBox="0 0 24 24"><path d="M3 13l6 6L22 4" fill="none" stroke="#6cc04a" stroke-width="4"/></svg><span><span class="service__name">BAS</span> - FKR Public BAS Practitioner</span></li>
    <li class="service"><svg viewBox="0 0 24 24"><path d="M3 13l6 6L22 4" fill="none" stroke="#6cc04a" stroke-width="4"/></svg><span><span class="service__name">Training &amp; support</span> - Tallivo Certified<br>Advisor</span></li>
    <li class="service"><svg viewBox="0 0 24 24"><path d="M3 13l6 6L22 4" fill="none" stroke="#6cc04a" stroke-width="4"/></svg><span><span class="service__name">Management reports</span></span></li>
    <li class="service"><svg viewBox="0 0 24 24"><path d="M3 13l6 6L22 4" fill="none" stroke="#6cc04a" stroke-width="4"/></svg><span><span class="service__name">Tax</span> - Dutyfile Near Member</span></li>
    <li class="service"><svg viewBox="0 0 24 24"><path d="M3 13l6 6L22 4" fill="none" stroke="#6cc04a" stroke-width="4"/></svg><span><span class="service__name">HR services</span></span></li>
  </ul>
</section>

<section class="card card--front" aria-label="Card front">
  <div class="wordmark front-title"><span class="wordmark__dot"></span><span>Ledgers On Track</span></div>
  <p class="abn">ABN 12 604 387 915</p>

  <div class="person">
    <p class="person__name">Martin Halloway</p>
    <p class="person__credentials">B Comm MA PhD AFKR<br>Registered BAS agent</p>
  </div>

  <div class="front-partners">
    <div class="org-name">Tallivo</div>
    <div class="badge badge--advisor" role="img" aria-label="Certified advisor badge"></div>
  </div>

  <ul class="contact">
    <li class="contact__phones">
      <span><i class="contact__icon"><svg viewBox="0 0 12 12"><path d="M2 1h3l1 3-2 1a6 6 0 0 0 3 3l1-2 3 1v3c-6 0-9-3-9-9z" fill="#fff"/></svg></i>03 9000 2741</span>
      <span><i class="contact__icon"><svg viewBox="0 0 12 12"><rect x="3" y="1" width="6" height="10" rx="1" fill="none" stroke="#fff" stroke-width="1.5"/></svg></i>0400 555 318</span>
    </li>
    <li><i class="contact__icon"><svg viewBox="0 0 12 12"><rect x="1" y="2.5" width="10" height="7" fill="#fff"/><path d="M1 3l5 4 5-4" fill="none" stroke="#5aaa3c" stroke-width="1"/></svg></i>martin@ledgersontrack.com</li>
    <li><i class="contact__icon"><svg viewBox="0 0 12 12"><circle cx="6" cy="6" r="4.5" fill="none" stroke="#fff" stroke-width="1.2"/><path d="M1.5 6h9M6 1.5v9" stroke="#fff" stroke-width="1"/></svg></i>www.ledgersontrack.com</li>
    <li><i class="contact__icon"><svg viewBox="0 0 12 12"><path d="M6 11S2 6.5 2 4.5a4 4 0 0 1 8 0C10 6.5 6 11 6 11z" fill="#fff"/><circle cx="6" cy="4.5" r="1.4" fill="#5aaa3c"/></svg></i><span>18 Larchmont Road<br>Greensborough VIC 3088</span></li>
  </ul>

  <div class="org-name front-fkr"><span class="org-name__square"></span>FKR</div>
  <div class="front-stripe"></div>
</section>

</body>
</html>
```